BRISKA sparkling water needs new artwork! Based in Southern California

"Briska" is a new sparkling water company based in Southern California that offers refreshing flavors (lime, cherry, & mango) with B vitamins and antioxidants.

We would like to see packaging designs for standard 12oz cans for each of the three flavors.
Our initial preference is to have individual artwork for each flavor.

Attached are examples of competitors' designs.
Updates

We are extending the deadline for the Thanksgiving Holiday. Thank you all for your contributions.

```html
<!DOCTYPE html>
<html lang="en">
<head>
<meta charset="utf-8">
<title>Briska Sparkling Water — Can Labels</title>
<link rel="stylesheet" href="https://fonts.googleapis.com/css2?family=Alfa+Slab+One&display=swap">
<style>
  :root {
    --backdrop: #ececec;
    --label: #fbfbfb;
    --ink: #1f1f1f;
    --lime: #c9d62b;
    --mango: #e2481f;
    --cherry: #c92a55;
  }
  * { margin: 0; padding: 0; box-sizing: border-box; }
  html, body {
    width: 1200px;
    height: 800px;
    overflow: hidden;
    background: var(--backdrop);
  }
  .lineup {
    width: 1200px;
    height: 800px;
    display: flex;
    justify-content: center;
    align-items: center;
    gap: 60px;
  }
  .can-label {
    position: relative;
    width: 300px;
    height: 600px;
    background: var(--label);
    border-radius: 6px;
    overflow: hidden;
    font-family: "Alfa Slab One", serif;
    color: var(--ink);
  }
  .flavor-burst {
    position: absolute;
    left: 10px;
    width: 280px;
    height: 280px;
  }
  .wordmark {
    position: absolute;
    left: 60px;
    writing-mode: vertical-rl;
    transform: rotate(180deg);
    font-size: 104px;
    line-height: 1;
    letter-spacing: -2px;
  }
  .flavor-name {
    position: absolute;
    left: 168px;
    font-size: 26px;
    line-height: 1;
  }
  .volume {
    position: absolute;
    bottom: 40px;
    left: 0;
    right: 0;
    text-align: center;
    font-size: 13px;
  }
  .can-label--lime .flavor-burst { top: 60px; }
  .can-label--lime .wordmark { bottom: 70px; }
  .can-label--lime .flavor-name { top: 228px; }

  .can-label--mango .flavor-burst { top: 150px; }
  .can-label--mango .wordmark { bottom: 70px; }
  .can-label--mango .flavor-name { top: 228px; }

  .can-label--cherry .flavor-burst { top: 280px; }
  .can-label--cherry .wordmark { top: 90px; }
  .can-label--cherry .flavor-name { top: 95px; }
</style>
</head>
<body>
  <main class="lineup">
    <section class="can-label can-label--lime">
      <svg class="flavor-burst" viewBox="0 0 280 280" role="img" aria-label="Lime coloured radiating burst pattern">
        <defs>
          <radialGradient id="lime-glow">
            <stop offset="0" stop-color="var(--lime)" stop-opacity="1"/>
            <stop offset="0.75" stop-color="var(--lime)" stop-opacity="0.85"/>
            <stop offset="1" stop-color="var(--lime)" stop-opacity="0"/>
          </radialGradient>
        </defs>
        <circle cx="140" cy="140" r="140" fill="url(#lime-glow)"/>
      </svg>
      <h2 class="wordmark">briska</h2>
      <p class="flavor-name">lime</p>
      <p class="volume">12oz</p>
    </section>

    <section class="can-label can-label--mango">
      <svg class="flavor-burst" viewBox="0 0 280 280" role="img" aria-label="Mango coloured radiating burst pattern">
        <defs>
          <radialGradient id="mango-glow">
            <stop offset="0" stop-color="var(--mango)" stop-opacity="1"/>
            <stop offset="0.75" stop-color="var(--mango)" stop-opacity="0.85"/>
            <stop offset="1" stop-color="var(--mango)" stop-opacity="0"/>
          </radialGradient>
        </defs>
        <circle cx="140" cy="140" r="140" fill="url(#mango-glow)"/>
      </svg>
      <h2 class="wordmark">briska</h2>
      <p class="flavor-name">mango</p>
      <p class="volume">12oz</p>
    </section>

    <section class="can-label can-label--cherry">
      <svg class="flavor-burst" viewBox="0 0 280 280" role="img" aria-label="Cherry coloured radiating burst pattern">
        <defs>
          <radialGradient id="cherry-glow">
            <stop offset="0" stop-color="var(--cherry)" stop-opacity="1"/>
            <stop offset="0.75" stop-color="var(--cherry)" stop-opacity="0.85"/>
            <stop offset="1" stop-color="var(--cherry)" stop-opacity="0"/>
          </radialGradient>
        </defs>
        <circle cx="140" cy="140" r="140" fill="url(#cherry-glow)"/>
      </svg>
      <h2 class="wordmark">briska</h2>
      <p class="flavor-name">cherry</p>
      <p class="volume">12oz</p>
    </section>
  </main>
</body>
</html>
```